Larkmoor Business Card Design Project

Double side card , just the logo on oxford white background on one side , and the rest of the information on the other side..
the company name is : Larkmoor Continental General Trading LLC.
logo is already attached
the card to show in the info side: company name, employee name and position (job title) phone number, fax number, email address, P.O. box, Location (city and country)
deadline is already extended 4 all to have more time... thanks

```html
<!DOCTYPE html>
<html lang="en">
<head>
<meta charset="utf-8">
<title>Larkmoor Continental – Business Card</title>
<link rel="stylesheet" href="https://fonts.googleapis.com/css2?family=Lato:wght@400;700&display=swap">
<style>
  :root {
    --backdrop: #e6e7e9;
    --card: #f4f5f6;
    --card-edge: #d5d7da;
    --ink: #2b2d30;
    --slate: #55585c;
    --brand-blue: #1f6f9c;
    --band-top: #36b3e3;
    --band-mid: #1a85b8;
    --band-bottom: #0d5578;
    --rule: #b9bcc0;
  }
  * { margin: 0; padding: 0; box-sizing: border-box; }
  html, body {
    width: 1200px; height: 620px; overflow: hidden;
    background: var(--backdrop);
    font-family: "Lato", Arial, sans-serif;
    color: var(--ink);
  }
  .sheet {
    position: relative; width: 1200px; height: 620px;
  }
  .card {
    position: absolute; left: 377px; width: 446px; height: 235px;
    background: var(--card);
    border: 1px solid var(--card-edge);
    box-shadow: 0 2px 6px rgba(0,0,0,.12);
    overflow: hidden;
  }
  .card--front { top: 36px; }
  .card--back { top: 328px; }

  /* front */
  .front-mark {
    position: absolute; left: 0; right: 0; top: 118px;
    display: flex; align-items: center; justify-content: center; gap: 12px;
  }
  .mark-dot {
    width: 14px; height: 14px; border-radius: 50%; background: var(--brand-blue);
  }
  .wordmark {
    font-weight: 700; letter-spacing: .5px; color: var(--slate);
  }
  .front-mark .wordmark { font-size: 36px; }
  .company-line {
    position: absolute; left: 0; right: 0;
    text-align: center; color: var(--brand-blue); font-size: 7px;
  }
  .card--front .company-line { top: 177px; }

  /* back */
  .contact-band {
    position: absolute; left: 0; top: 0; bottom: 0; width: 46px;
    background: linear-gradient(180deg, var(--band-top) 0%, var(--band-mid) 45%, var(--band-bottom) 100%);
  }
  .band-icons {
    position: absolute; left: 26px; top: 96px;
    display: flex; flex-direction: column; gap: 6px;
  }
  .band-icons svg { width: 14px; height: 14px; display: block; }
  .person {
    position: absolute; left: 58px; top: 44px;
  }
  .person-name { font-size: 15px; }
  .person-role { font-size: 12px; color: var(--brand-blue); margin-top: 1px; }
  .contact-list {
    position: absolute; left: 58px; top: 95px; list-style: none;
    font-size: 13px; line-height: 19.5px;
  }
  .contact-list .email { font-size: 12px; margin-top: 3px; }
  .contact-list .web { font-size: 12px; color: var(--brand-blue); }
  .divider {
    position: absolute; left: 200px; top: 42px; height: 152px; width: 1px;
    background: var(--rule);
  }
  .back-mark {
    position: absolute; left: 200px; right: 0; top: 78px;
    display: flex; align-items: center; justify-content: center; gap: 8px;
  }
  .back-mark .mark-dot { width: 9px; height: 9px; }
  .back-mark .wordmark { font-size: 22px; }
  .card--back .company-line { left: 200px; top: 136px; font-size: 7px; }
  .address {
    position: absolute; left: 200px; right: 0; top: 148px;
    text-align: center; font-size: 5.5px; line-height: 8px; color: var(--slate);
  }
</style>
</head>
<body>
<main class="sheet">
  <section class="card card--front" aria-label="Card front">
    <div class="front-mark">
      <span class="mark-dot"></span>
      <span class="wordmark">Larkmoor Int.</span>
    </div>
    <p class="company-line">Larkmoor Continental General Trading LLC</p>
  </section>

  <section class="card card--back" aria-label="Card back">
    <div class="contact-band">
      <div class="band-icons">
        <svg viewBox="0 0 14 14" aria-label="Phone"><circle cx="7" cy="7" r="6.3" fill="none" stroke="#fff" stroke-width=".8"/><path d="M5 4.2c-.6.4-.7 1.3 0 2.6s1.8 2.4 2.9 2.8c.8.3 1.4 0 1.6-.5l-1.1-.9-.6.5c-.6-.3-1.3-1-1.6-1.6l.5-.6-.8-1.1z" fill="#fff"/></svg>
        <svg viewBox="0 0 14 14" aria-label="Mobile"><circle cx="7" cy="7" r="6.3" fill="none" stroke="#fff" stroke-width=".8"/><rect x="5.2" y="3.6" width="3.6" height="6.8" rx=".6" fill="none" stroke="#fff" stroke-width=".8"/></svg>
        <svg viewBox="0 0 14 14" aria-label="Fax"><circle cx="7" cy="7" r="6.3" fill="none" stroke="#fff" stroke-width=".8"/><rect x="4" y="6" width="6" height="3.6" fill="none" stroke="#fff" stroke-width=".8"/><rect x="5" y="3.8" width="4" height="2.2" fill="none" stroke="#fff" stroke-width=".7"/></svg>
        <svg viewBox="0 0 14 14" aria-label="Email"><circle cx="7" cy="7" r="6.3" fill="none" stroke="#fff" stroke-width=".8"/><rect x="4" y="4.8" width="6" height="4.4" fill="none" stroke="#fff" stroke-width=".8"/><path d="M4 4.8l3 2.4 3-2.4" fill="none" stroke="#fff" stroke-width=".7"/></svg>
        <svg viewBox="0 0 14 14" aria-label="Website"><circle cx="7" cy="7" r="6.3" fill="none" stroke="#fff" stroke-width=".8"/><circle cx="7" cy="7" r="3.2" fill="none" stroke="#fff" stroke-width=".7"/><path d="M3.8 7h6.4M7 3.8v6.4" stroke="#fff" stroke-width=".6"/></svg>
      </div>
    </div>

    <div class="person">
      <p class="person-name">Daniel Reeve</p>
      <p class="person-role">CEO</p>
    </div>
    <ul class="contact-list">
      <li>01632 960 418</li>
      <li>07700 900 512</li>
      <li>01632 960 733</li>
      <li class="email">daniel@larkmoorintl.com</li>
      <li class="web">www.larkmoorintl.com</li>
    </ul>

    <div class="divider"></div>

    <div class="back-mark">
      <span class="mark-dot"></span>
      <span class="wordmark">Larkmoor Int.</span>
    </div>
    <p class="company-line">Larkmoor Continental General Trading LLC</p>
    <address class="address">
      48 Harrow Quay Road<br>Eastfield<br>Northshire<br>UK<br>EF4 2LQ
    </address>
  </section>
</main>
</body>
</html>
```